TAILWIND FIELDS Pet Resorts Outdoor Signage

4 x 8 outdoor signage design for our two locations

Target Market(s)

Existing and New Customers

Industry/Entity Type

Pet Care

Font styles to use
Sans Serif

Colors

Designer to choose colors to be used in the design.

```html
<!DOCTYPE html>
<html lang="en">
<head>
<meta charset="utf-8">
<title>Tailwind Fields Social Club Sign</title>
<link rel="stylesheet" href="https://fonts.googleapis.com/css2?family=Anton&family=Montserrat:wght@600;700;800&family=Open+Sans:wght@400&display=swap">
<style>
  :root {
    --stage: #e4e4e4;
    --sign-dark: #212121;
    --silhouette: #121212;
    --brand-orange: #f8ad43;
    --white: #ffffff;
  }
  * { margin: 0; padding: 0; box-sizing: border-box; }
  html, body {
    width: 1200px; height: 1200px; overflow: hidden;
    background: var(--stage);
  }
  .sign {
    position: absolute; left: 24px; top: 375px;
    width: 1152px; height: 576px;
    background: var(--sign-dark);
    overflow: hidden;
  }
  .sign__bottom-band {
    position: absolute; left: 0; right: 0; bottom: 0; height: 23px;
    background: var(--brand-orange);
  }
  .sign__dog-art {
    position: absolute; left: 840px; top: 0; width: 312px; height: 553px;
    background: linear-gradient(90deg, rgba(18,18,18,0) 0%, var(--silhouette) 30%, var(--silhouette) 100%);
    opacity: 0.85;
  }
  .brand {
    position: absolute; left: 53px; top: 30px; width: 385px;
    font-family: "Montserrat", sans-serif;
  }
  .brand__name {
    color: var(--brand-orange);
    font-weight: 800;
    font-size: 78px;
    line-height: 0.98;
    letter-spacing: -1px;
    height: 380px;
    display: flex; flex-direction: column; justify-content: flex-end;
    padding-bottom: 22px;
  }
  .brand__rule {
    height: 6px; width: 287px; background: var(--brand-orange);
  }
  .brand__club {
    color: var(--white);
    font-weight: 600;
    font-size: 38px;
    letter-spacing: 2px;
    line-height: 1;
    padding: 12px 0 10px;
  }
  .brand__campus {
    margin-top: 10px;
    color: var(--white);
    font-family: "Open Sans", sans-serif;
    font-size: 22px;
    letter-spacing: -0.3px;
  }
  .headline {
    position: absolute; left: 431px; top: 112px; width: 688px;
    font-family: "Anton", sans-serif;
    text-align: center;
    text-transform: uppercase;
    white-space: nowrap;
  }
  .headline__top {
    color: var(--white);
    font-size: 122px; line-height: 116px;
    letter-spacing: 1px;
  }
  .headline__bottom {
    color: var(--brand-orange);
    font-size: 124px; line-height: 118px;
    letter-spacing: 1px;
  }
  .headline__rule {
    position: absolute; left: 431px; top: 367px;
    width: 688px; height: 14px; background: var(--brand-orange);
  }
  .contact {
    position: absolute; left: 431px; top: 400px; width: 688px;
    text-align: center;
    font-family: "Montserrat", sans-serif;
    font-weight: 700;
    color: var(--white);
    white-space: nowrap;
  }
  .contact__phone { font-size: 58px; line-height: 72px; letter-spacing: -1px; }
  .contact__web { font-size: 52px; line-height: 70px; letter-spacing: -1px; }
</style>
</head>
<body>
  <div class="sign">
    <div class="sign__dog-art" role="img" aria-label="Large dark silhouette of a sitting dog"></div>

    <div class="brand">
      <div class="brand__name">TAILWIND<br>FIELDS</div>
      <div class="brand__rule"></div>
      <div class="brand__club">SOCIAL CLUB</div>
      <div class="brand__rule"></div>
      <div class="brand__campus">East Hollowbrook Campus</div>
    </div>

    <h1 class="headline">
      <div class="headline__top">Home to the</div>
      <div class="headline__bottom">Social Club</div>
    </h1>
    <div class="headline__rule"></div>

    <div class="contact">
      <div class="contact__phone">555-014-2876</div>
      <div class="contact__web">www.tailwindfields.ca</div>
    </div>

    <div class="sign__bottom-band"></div>
  </div>
</body>
</html>
```